Brenvick Holdings LLC, new Business cards

I'm moving offices and need new cards. Plus I'm open to modifying the current design of my card. I will keep the logo but would like to explore other layouts and fonts for the design. I've included the current double sided card for reference. I Like the navy color and white. Might be open to grays or silver. Needs to be clean and elegant.

Target Market(s)

Investors, buyers & sellers of private equities and real estate.

Contact Information for Business Card

Brenvick Holdings
Dorian P.K. Halvers, Managing Principal
418 Ostrander Ave., Suite 612
Denver, CO 80319
M: 970-555-0147, O: 303-555-0192
Dorian@brenvickholdings.example
Brenvickholdings.example

Colors
0354a2
ffffff
c4c4c4

Requirements
Must have
• Business card details.
• Logo raised or embossed, it was designed after a wax seal. Current has raised ink.
Nice to have
• Space on card to write additional notes.

```html
<!DOCTYPE html>
<html lang="en">
<head>
<meta charset="utf-8">
<title>Brenvick Holdings – Business Card</title>
<link href="https://fonts.googleapis.com/css2?family=Montserrat:wght@800&family=Open+Sans:wght@400;600&display=swap" rel="stylesheet">
<style>
  :root {
    --navy: #221c5c;
    --white: #ffffff;
    --silver: #c4c4c4;
    --grey-text: #8a8a8a;
    --backdrop: #e8e8eb;
  }
  * { margin: 0; padding: 0; box-sizing: border-box; }
  html, body { width: 847px; height: 1200px; overflow: hidden; }
  body {
    background: var(--backdrop);
    position: relative;
    font-family: "Open Sans", Arial, sans-serif;
  }
  .card {
    position: absolute;
    left: 63px;
    width: 720px;
    height: 412px;
    border-radius: 26px;
    overflow: hidden;
    background: var(--white);
    box-shadow: 0 6px 18px rgba(0,0,0,0.18);
  }
  .card--front { top: 150px; }
  .card--back { top: 640px; }
  .card__shapes { position: absolute; inset: 0; }

  .holder { position: absolute; left: 54px; top: 40px; }
  .holder__name {
    font-family: "Montserrat", Arial, sans-serif;
    font-weight: 800;
    font-size: 23px;
    letter-spacing: 0.3px;
    color: var(--navy);
    text-transform: uppercase;
  }
  .holder__title { font-size: 17px; color: var(--grey-text); margin-top: 2px; }

  .contacts { position: absolute; left: 54px; top: 128px; list-style: none; }
  .contacts li {
    display: flex; align-items: center; gap: 10px;
    font-size: 15.5px; color: var(--navy); line-height: 25px;
  }
  .contacts svg { width: 13px; height: 13px; fill: var(--grey-text); flex: none; }

  .address {
    position: absolute; left: 30px; top: 262px;
    display: flex; gap: 10px;
    color: var(--white); font-size: 16px; line-height: 25px;
  }
  .address svg { width: 14px; height: 18px; fill: var(--silver); margin-top: 3px; flex: none; }

  .website {
    position: absolute; left: 40px; top: 300px;
    color: var(--white); font-size: 21px; letter-spacing: 1.2px;
  }

  .brand {
    position: absolute;
    display: flex; align-items: center; justify-content: center;
    border-radius: 50%;
    background: var(--navy);
    border: 9px solid var(--white);
    color: var(--white);
    font-family: "Open Sans", Arial, sans-serif;
    font-weight: 600;
    text-align: center;
    text-transform: uppercase;
    letter-spacing: 2px;
  }
  .card--front .brand { left: 500px; top: 208px; width: 184px; height: 184px; font-size: 17px; line-height: 26px; }
  .card--back .brand { left: 540px; top: 255px; width: 146px; height: 146px; font-size: 13px; line-height: 20px; border-width: 7px; }
</style>
</head>
<body>

<section class="card card--front">
  <svg class="card__shapes" viewBox="0 0 720 412" aria-hidden="true">
    <path d="M0,218 H390 C470,218 500,176 570,170 L720,160 V412 H0Z" fill="var(--silver)"/>
    <path d="M0,230 H390 C470,230 505,190 575,184 L720,176 V412 H0Z" fill="var(--navy)"/>
  </svg>

  <div class="holder">
    <h1 class="holder__name">Dorian P.K. Halvers</h1>
    <p class="holder__title">Managing Principal</p>
  </div>

  <ul class="contacts">
    <li><svg viewBox="0 0 24 24"><path d="M6.6 10.8a15.1 15.1 0 0 0 6.6 6.6l2.2-2.2c.3-.3.7-.4 1-.2 1.1.4 2.3.6 3.6.6.6 0 1 .4 1 1V20c0 .6-.4 1-1 1A17 17 0 0 1 3 4c0-.6.4-1 1-1h3.5c.6 0 1 .4 1 1 0 1.3.2 2.5.6 3.6.1.3 0 .7-.2 1z"/></svg>M: 970-555-0147, O: TBD</li>
    <li><svg viewBox="0 0 24 24"><path d="M2 5h20v14H2z M4 7v.5l8 5 8-5V7l-8 5z" fill-rule="evenodd"/></svg>Dorian@brenvickholdings.example</li>
    <li><svg viewBox="0 0 24 24"><circle cx="12" cy="12" r="10"/></svg>Brenvickholdings.example</li>
  </ul>

  <div class="address">
    <svg viewBox="0 0 14 18"><path d="M7 0a7 7 0 0 0-7 7c0 5 7 11 7 11s7-6 7-11a7 7 0 0 0-7-7zm0 9.5A2.5 2.5 0 1 1 7 4.5a2.5 2.5 0 0 1 0 5z"/></svg>
    <p>418 Ostrander Ave., Suite 612<br>Denver, CO 80319</p>
  </div>

  <div class="brand">Brenvick<br>Holdings</div>
</section>

<section class="card card--back">
  <svg class="card__shapes" viewBox="0 0 720 412" aria-hidden="true">
    <path d="M0,232 H720 V412 H0Z" fill="var(--navy)"/>
  </svg>
  <p class="website">WWW.BRENVICKHOLDINGS.EXAMPLE</p>
  <div class="brand">Brenvick<br>Holdings</div>
</section>

</body>
</html>
```